Advertisement for back of sporting brochure

Company: Gridiron Ascent / gridascentpro.example
Business: Football skills development for offensive and defensive positions
Slogan: Learn to play the game on and off the field
Company colors: Royal Blue (reflex blue), White, Cool Gray 11 or Cool Gray 4, safety green can be used for some highlighting
Phone#: 555-274-8813

We require an 8.5" x 11" size flyer advertising the company.
The flyer will be displayed on the back of a sporting event program.
The objective of the flyer is to get viewers to contact Gridiron Ascent by either website or phone.

Must have items in the flyer are:
* Logo
* Slogan (see above)
* website (see above)
* Phone #
* photos
* Testimonials
* Word from the owner (see below)

“ In just 3 short years Gridiron Ascent clients have shown that skill development with the coaches at GA works! Over these past 3 years GA has had 24 players in the Continental Pigskin Circuit and 28 players go on to play at the collegiate level. We are making an impact on teams at every level including the 2013 High School State Championships with over 20 players participating in the state games. We have also worked with young players producing the MVP and Captains of the 2013 OKYA State champion. If you want to surround yourself with winners and raise your level of play while having fun and gaining confidence call us today!"

The CALL TO ACTION (CTA) is critical! The objective is for the viewer to call the phone number provided, now! The CTA should not fall into the same paragraph as information verbiage.

Target Market(s)

Elementary, Middle & High School players and parents

Industry/Entity Type

Advertising

Requirements
Must have
• CALL TO ACTION (CTA)
Readers must themselves, want to be part of the Gridiron Ascent family
OR
The parent must want their student athlete to become the best football player they can be
Should not have
• RED

```html
<!DOCTYPE html>
<html lang="en">
<head>
<meta charset="utf-8">
<title>Gridiron Ascent – Football Skills Development</title>
<link rel="stylesheet" href="https://fonts.googleapis.com/css2?family=Arimo:ital,wght@0,400;0,700;1,400;1,700&display=swap">
<style>
  :root {
    --royal-blue: #26379a;
    --safety-green: #6dbe4b;
    --ink: #111111;
    --cool-gray: #5a5d63;
    --paper: #ffffff;
    --field-green: #4f7f3a;
    --turf-dark: #3c5e2c;
    --arena-gray: #9a9ca3;
    --jersey-navy: #23335c;
    --jersey-orange: #d8692a;
    --training-floor: #6a8a4a;
    --wall-red: #7b6e6e;
  }
  * { box-sizing: border-box; margin: 0; padding: 0; }
  html, body { width: 927px; height: 1200px; overflow: hidden; background: var(--paper); }
  body { font-family: "Arimo", Arial, sans-serif; color: var(--ink); }

  .flyer { position: relative; width: 927px; height: 1200px; background: var(--paper); }

  .headline {
    position: absolute; top: -4px; left: 0; width: 100%;
    text-align: center; color: var(--royal-blue);
    font-weight: 700; font-size: 68px; line-height: 68px; letter-spacing: -0.5px;
  }

  .team-photo {
    position: absolute; left: 18px; top: 147px; width: 891px; height: 250px;
    background: linear-gradient(180deg, var(--arena-gray) 0%, #c9cbcf 30%, var(--safety-green) 55%, var(--field-green) 80%, var(--turf-dark) 100%);
  }

  .mission {
    position: absolute; left: 20px; top: 404px; width: 887px;
    text-align: center; font-size: 22.5px; line-height: 25px;
  }

  .cta {
    position: absolute; left: 0; top: 512px; width: 100%;
    text-align: center; color: var(--safety-green);
    font-weight: 700; font-size: 46px; line-height: 56px;
  }

  .action-photo {
    position: absolute; left: 58px; top: 603px; width: 814px; height: 330px;
    background: linear-gradient(100deg, var(--jersey-navy) 0%, var(--jersey-orange) 35%, #2b2f3a 55%, #e7e9ee 75%, var(--jersey-navy) 100%);
  }

  .drill-photo {
    position: absolute; top: 742px; height: 192px;
    border: 3px solid var(--paper);
  }
  .drill-photo--left {
    left: 134px; width: 314px;
    background: linear-gradient(180deg, #b9b6b0 0%, #8d8a84 40%, var(--training-floor) 60%, var(--field-green) 100%);
  }
  .drill-photo--right {
    left: 460px; width: 330px;
    background: linear-gradient(180deg, var(--wall-red) 0%, #a9a5a2 35%, var(--training-floor) 55%, var(--field-green) 100%);
  }

  .brand-block { position: absolute; left: 48px; top: 950px; width: 380px; text-align: center; }
  .brand-mark {
    display: flex; align-items: center; justify-content: center; gap: 14px;
    height: 108px;
  }
  .brand-mark__dot { width: 34px; height: 34px; border-radius: 50%; background: var(--royal-blue); flex: none; }
  .brand-mark__name { color: var(--royal-blue); font-weight: 700; font-size: 38px; line-height: 1; }
  .brand-address { font-size: 15px; line-height: 20px; margin-top: 8px; }
  .brand-phone { font-weight: 700; font-size: 27px; line-height: 34px; margin-top: 6px; }
  .brand-web { font-weight: 700; font-size: 25px; line-height: 32px; margin-top: 4px; }

  .owner-word {
    position: absolute; left: 462px; top: 950px; width: 448px;
    font-size: 11.6px; line-height: 16px;
  }
  .owner-word__quote { font-weight: 700; }
  .owner-word__sign { font-style: italic; font-weight: 700; }
</style>
</head>
<body>
<main class="flyer">
  <h1 class="headline">Gridiron Ascent<br>At It’s Best</h1>

  <div class="team-photo" role="img" aria-label="Group photo of coaches in white shirts and young players in green shirts on an indoor turf field"></div>

  <p class="mission">We develop and nurture the football skills of young Scholar Athletes providing academic support, recruiting assistance, motivation, encouragement and life skills development. Get the skills you need to play at the next level.<br>Learn to play the game on and off the field.</p>

  <p class="cta">Call Us Today: 555-274-8813</p>

  <div class="action-photo" role="img" aria-label="Professional linemen in orange, navy and white uniforms clashing at the line of scrimmage"></div>
  <div class="drill-photo drill-photo--left" role="img" aria-label="Players running agility drills over red pads in an indoor training facility"></div>
  <div class="drill-photo drill-photo--right" role="img" aria-label="Young players in green shirts working through a pad drill on indoor turf"></div>

  <section class="brand-block">
    <div class="brand-mark">
      <span class="brand-mark__dot"></span>
      <span class="brand-mark__name">Gridiron Ascent</span>
    </div>
    <p class="brand-address">2480 W. Meridian Avenue Fairhaven, IN 46099</p>
    <p class="brand-phone">555-274-8813</p>
    <p class="brand-web">www.gridascentpro.example</p>
  </section>

  <section class="owner-word">
    <p class="owner-word__quote">“In just 3 short years Gridiron Ascent clients have shown that skill development with the coaches at GA works! Over these past 3 years GA has had 24 players in the Continental Pigskin Circuit and 28 players go on to play at the collegiate level. We are making an impact on teams at every level including the 2013 High School State Championships with over 20 players participating in the state games. We have also worked with young players producing the MVP and Captains of the 2013 OKYA State champion. If you want to surround yourself with winners and raise your level of play while having fun and gaining confidence call us today!”</p>
    <p class="owner-word__sign">Coach Harlan is the head coach with over 20 years of football coaching experience.</p>
  </section>
</main>
</body>
</html>
```